business card design for luxurious real estate brand

using the attached logo, i am looking for a 2-sided business card design. the back should be the gold logo on black background. the front needs to include: gold logo, name, phone, email, and website

Industry/Entity Type

real estate

Contact Information for Business Card

logo, name, email, phone, website

Font styles to use
Sans Serif

```html
<!DOCTYPE html>
<html lang="en">
<head>
<meta charset="utf-8">
<title>Casa Solenne — Business Card</title>
<link rel="stylesheet" href="https://fonts.googleapis.com/css2?family=Arimo:wght@400;700&display=swap">
<style>
  :root {
    --canvas: #1a1a1a;
    --card: #262527;
    --card-glow: #3a393b;
    --gold: #fdc80a;
    --white: #ffffff;
  }
  * { margin: 0; padding: 0; box-sizing: border-box; }
  html, body {
    width: 1200px; height: 900px; overflow: hidden;
    background: var(--canvas);
    font-family: "Arimo", Arial, sans-serif;
  }
  .sheet {
    width: 1200px; height: 900px;
    display: flex; flex-direction: column;
    align-items: center; justify-content: center; gap: 36px;
  }
  .card {
    position: relative;
    width: 700px; height: 400px;
    background: var(--card);
    overflow: hidden;
    box-shadow: 0 14px 30px rgba(0,0,0,0.55);
  }
  .card__glow {
    position: absolute;
    right: -40px; top: -40px;
    width: 420px; height: 420px;
    background: radial-gradient(circle at 45% 45%, var(--card-glow) 0%, rgba(58,57,59,0) 65%);
  }
  .brand {
    position: absolute;
    display: flex; align-items: center; gap: 14px;
    color: var(--gold);
    font-weight: 400;
    letter-spacing: 0.32em;
    text-transform: uppercase;
    white-space: nowrap;
  }
  .brand__mark {
    display: block;
    background: var(--gold);
  }
  .card--back .brand {
    left: 50%; top: 50%;
    transform: translate(-50%, -50%);
    font-size: 40px;
  }
  .card--back .brand__mark { width: 30px; height: 30px; }
  .card--front .brand {
    left: 56px; top: 58px;
    font-size: 26px;
  }
  .card--front .brand__mark { width: 20px; height: 20px; }
  .person {
    position: absolute;
    left: 56px; top: 168px;
  }
  .person__name {
    color: var(--gold);
    font-weight: 700;
    font-size: 30px;
    line-height: 1.1;
  }
  .person__title {
    color: var(--white);
    font-weight: 700;
    font-size: 18px;
    margin-top: 2px;
  }
  .contacts {
    position: absolute;
    left: 56px; top: 250px;
    list-style: none;
  }
  .contacts__item {
    display: flex; align-items: center; gap: 14px;
    color: var(--white);
    font-weight: 700;
    font-size: 19px;
    height: 34px;
  }
  .contacts__icon { width: 20px; height: 20px; flex: none; }
</style>
</head>
<body>
<main class="sheet">

  <section class="card card--back" aria-label="Card back">
    <div class="card__glow"></div>
    <div class="brand"><span class="brand__mark"></span>Casa Solenne</div>
  </section>

  <section class="card card--front" aria-label="Card front">
    <div class="card__glow"></div>
    <div class="brand"><span class="brand__mark"></span>Casa Solenne</div>

    <div class="person">
      <p class="person__name">Daniel Marsh</p>
      <p class="person__title">Your Title</p>
    </div>

    <ul class="contacts">
      <li class="contacts__item">
        <svg class="contacts__icon" viewBox="0 0 24 24" aria-hidden="true">
          <path fill="#fdc80a" d="M6.6 10.8a15.1 15.1 0 0 0 6.6 6.6l2.2-2.2a1 1 0 0 1 1-.25 11.4 11.4 0 0 0 3.6.57 1 1 0 0 1 1 1V20a1 1 0 0 1-1 1A17 17 0 0 1 3 4a1 1 0 0 1 1-1h3.5a1 1 0 0 1 1 1c0 1.25.2 2.45.57 3.57a1 1 0 0 1-.25 1z"/>
        </svg>
        (555) 204 318
      </li>
      <li class="contacts__item">
        <svg class="contacts__icon" viewBox="0 0 24 24" aria-hidden="true">
          <rect x="2" y="5" width="20" height="14" fill="#fdc80a"/>
          <path d="M2 5l10 8 10-8" fill="none" stroke="#262527" stroke-width="1.6"/>
        </svg>
        daniel@casasolenne.com
      </li>
      <li class="contacts__item">
        <svg class="contacts__icon" viewBox="0 0 24 24" aria-hidden="true">
          <g fill="none" stroke="#fdc80a" stroke-width="1.8">
            <circle cx="12" cy="12" r="9.5"/>
            <ellipse cx="12" cy="12" rx="4.5" ry="9.5"/>
            <path d="M2.5 12h19M4 7h16M4 17h16"/>
          </g>
        </svg>
        www.casasolenne.com
      </li>
    </ul>
  </section>

</main>
</body>
</html>
```